School Poster

Design so that these can be placed in classrooms across the school.

Attached is another design we have had done. Use a similar theme.

Consider using themes from https://calderwoodhs.lumorin.edu/

please edit Binder1 doc.

Target Market(s)

Students and teachers

```html
<!DOCTYPE html>
<html lang="en">
<head>
<meta charset="utf-8">
<title>Before You Ask the Teacher</title>
<link href="https://fonts.googleapis.com/css2?family=Poppins:wght@400;500;600;700;800&display=swap" rel="stylesheet">
<style>
:root{
  --navy:#172a45;
  --gold:#fcc200;
  --gold-text:#d9a300;
  --cream:#fdf8e8;
  --ice:#e6eefa;
  --grey:#e6e6e6;
  --white:#ffffff;
  --red:#e0282e;
}
*{margin:0;padding:0;box-sizing:border-box}
html,body{width:918px;height:1200px;overflow:hidden;background:var(--white)}
body{font-family:'Poppins',sans-serif;color:var(--navy);position:relative}
.poster{position:absolute;inset:0;width:918px;height:1200px;overflow:hidden}
.grey-zone{position:absolute;left:0;top:636px;width:918px;height:477px;background:var(--grey)}

/* header */
.brand{position:absolute;left:190px;top:60px;width:120px;display:flex;align-items:center;gap:8px}
.brand-mark{width:18px;height:18px;background:var(--navy);flex:none}
.brand-name{font-weight:700;font-size:15px;line-height:1.15;color:var(--navy)}
.title{position:absolute;left:333px;top:44px;font-weight:800;font-size:42px;line-height:1;letter-spacing:-.5px}
.title .gold{color:var(--gold);display:block}
.title .dark{color:var(--navy);display:block;margin-top:2px}

/* bands */
.band{position:absolute;left:49px;width:823px;background:var(--navy);color:var(--white);border-radius:12px 12px 0 0;text-align:center;font-weight:700}
.band-steps{top:154px;height:53px;font-size:24px;line-height:53px}
.band-ai{top:613px;height:53px;font-size:25px;line-height:53px}

/* steps */
.steps{position:absolute;left:49px;top:207px;width:823px;height:322px;display:flex}
.step{width:274.3px;height:100%;position:relative;padding:0 20px}
.step.cream{background:var(--cream)}
.step.ice{background:var(--ice)}
.step-rule{position:absolute;left:0;right:0;top:104px;border-top:1px dotted #9aa3b0}
.step-icon{position:absolute;left:50%;top:17px;transform:translateX(-50%);width:60px;height:60px}
.icon-fill{border-radius:50%;background:radial-gradient(circle,#c9d0da,#e9ecf1)}
.step-num{position:absolute;left:50%;top:89px;transform:translateX(-50%);width:32px;height:32px;border-radius:50%;font-weight:600;font-size:19px;line-height:32px;text-align:center}
.num-gold{background:var(--gold);color:var(--navy)}
.num-navy{background:var(--navy);color:var(--gold)}
.step-title{position:absolute;left:22px;top:136px;font-weight:700;font-size:17px}
.step-title.gold{color:var(--gold)}
.step-body{position:absolute;left:22px;right:14px;top:166px}
.lead{font-weight:700;font-size:13px;margin-bottom:8px;line-height:1.3}
.lead.gold{color:var(--gold-text)}
.ticks{list-style:none}
.ticks li{position:relative;padding-left:18px;font-size:10px;line-height:1.25;margin-bottom:9px}
.ticks li::before{content:"";position:absolute;left:0;top:1px;width:11px;height:11px;border-radius:50%;background:var(--navy)}
.ticks li::after{content:"";position:absolute;left:3.5px;top:3.5px;width:3px;height:5px;border:solid var(--white);border-width:0 1.5px 1.5px 0;transform:rotate(45deg)}
.ticks.gold li::before{background:var(--gold)}
.note{font-size:10px;margin-top:2px}

/* motto buttons */
.motto{position:absolute;top:545px;width:180px;height:35px;font-weight:600;font-size:14px;line-height:35px;text-align:center;border-radius:3px}
.motto::after{content:"";position:absolute;right:-28px;top:5px;border-left:22px solid var(--navy);border-top:12px solid transparent;border-bottom:12px solid transparent}
.motto.navy{background:var(--navy);color:var(--white)}
.motto.gold{background:var(--gold);color:var(--navy)}
.motto.gold::after{border-left-color:var(--gold)}

/* AI boxes */
.rules{position:absolute;top:672px;height:167px}
.rules-must{left:49px;width:410px;background:var(--cream);border:1px dashed #e6d37a}
.rules-help{left:463px;width:409px;background:var(--ice);border:1px dashed #5b6b84}
.rules h3{font-weight:700;font-size:17px;line-height:1.25}
.rules-must h3{position:absolute;left:20px;top:26px}
.rules-help h3{position:absolute;left:29px;top:26px}
.rules .col{position:absolute;width:170px}
.rules .ticks li{font-size:9.5px;margin-bottom:8px;line-height:1.2}

/* cannot do */
.divider{position:absolute;left:49px;width:823px;top:886px;border-top:1px solid #b9bcc2}
.cannot{position:absolute;left:367px;top:869px;width:187px;height:34px;background:var(--gold);border-radius:17px;font-weight:700;font-size:16px;line-height:34px;text-align:center}
.pieces{position:absolute;left:49px;top:930px;width:823px;height:118px;display:flex}
.piece{width:205.75px;height:100%;position:relative;display:flex;align-items:center;justify-content:center;text-align:center;font-size:12px;line-height:1.25;padding:20px 24px 0}
.piece span{position:relative;z-index:2}
.piece.gold{background:var(--gold);color:var(--navy)}
.piece.navy{background:var(--navy);color:var(--white)}
.knob{position:absolute;top:39px;width:44px;height:44px;border-radius:50%;z-index:1}
.knob.right{right:-22px}
.knob.left{left:-22px}
.knob.gold{background:var(--gold)}
.knob.navy{background:var(--navy)}
.no{position:absolute;left:50%;top:-19px;transform:translateX(-50%);width:38px;height:38px;z-index:3}

/* footer */
.slogan{position:absolute;left:225px;top:1088px;width:480px;height:40px;background:var(--gold);border-radius:20px 20px 0 0;font-size:14.5px;text-align:center;line-height:30px}
.footer{position:absolute;left:0;top:1113px;width:918px;height:87px;background:var(--navy);color:var(--white);text-align:center;font-size:6px;line-height:1.45;text-transform:uppercase;padding-top:33px;font-weight:500}
</style>
</head>
<body>
<main class="poster">
  <div class="grey-zone"></div>

  <div class="brand">
    <span class="brand-mark"></span>
    <span class="brand-name">Calderwood High</span>
  </div>
  <h1 class="title"><span class="gold">BEFORE YOU ASK</span><span class="dark">THE TEACHER...</span></h1>

  <h2 class="band band-steps">TRY THESE STEPS FIRST!</h2>
  <section class="steps">
    <div class="step cream">
      <div class="step-icon icon-fill" role="img" aria-label="Icon of a head with a thinking brain"></div>
      <div class="step-rule"></div>
      <div class="step-num num-gold">1</div>
      <h3 class="step-title">THINK FIRST</h3>
      <div class="step-body">
        <p class="lead gold">Don't give up straigh way.</p>
        <ul class="ticks">
          <li>Read the question carefully.</li>
          <li>Identify what you already know.</li>
          <li>Try a strategy you've used before.</li>
          <li>Give yourself thinking time.</li>
        </ul>
      </div>
    </div>
    <div class="step ice">
      <svg class="step-icon" viewBox="0 0 60 60" aria-hidden="true" fill="none" stroke="var(--gold)" stroke-width="1.8">
        <rect x="8" y="10" width="30" height="38" rx="1"/>
        <path d="M13 6h26l8 8v30"/>
        <path d="M14 20h18M14 26h18M14 32h12M14 38h10"/>
        <circle cx="44" cy="38" r="8" fill="var(--ice)"/>
        <path d="M40 38l3 3 5-6"/>
      </svg>
      <div class="step-rule"></div>
      <div class="step-num num-navy">2</div>
      <h3 class="step-title gold">CHECK YOUR -UPPORTS</h3>
      <div class="step-body">
        <p class="lead">Before asking for help, check:</p>
        <ul class="ticks gold">
          <li>Learning goal and success criteria.</li>
          <li>Worked examples.</li>
          <li>Class notes.</li>
          <li>Classroom displays.</li>
          <li>StudyHub resources.</li>
          <li>Task sheet and instructions.</li>
        </ul>
      </div>
    </div>
    <div class="step cream">
      <div class="step-icon icon-fill" role="img" aria-label="Icon of two people exchanging a question and a tick"></div>
      <div class="step-rule"></div>
      <div class="step-num num-gold">3</div>
      <h3 class="step-title">ASK 3 BEFORE ME</h3>
      <div class="step-body">
        <p class="lead gold">Ask three sources before asking the teacher:</p>
        <ul class="ticks">
          <li>A person (partner or neighbour)</li>
          <li>A place (notes, display, StudyHub)</li>
          <li>A resource (worked example, task sheet)</li>
        </ul>
        <p class="note">Then ask the teacher if you still need help.</p>
      </div>
    </div>
  </section>

  <div class="motto navy" style="left:90px">WE BELIEVE</div>
  <div class="motto gold" style="left:365px">WE STRIVE</div>
  <div class="motto navy" style="left:639px">WE ACHIEVE</div>

  <h2 class="band band-ai">USING AI AND OTHER TOOLS RESPONSIBLY</h2>

  <section class="rules rules-must">
    <h3>What You Must Do:</h3>
    <ul class="ticks col" style="left:20px;top:64px">
      <li>Complete your own work</li>
      <li>Demonstrate your progress (drafts, notes, planning, revisions)</li>
    </ul>
    <ul class="ticks col" style="left:207px;top:66px;width:180px">
      <li>Use feedback to improve your work</li>
      <li>Demonstrate your understanding of the ideas in your submission</li>
    </ul>
  </section>
  <section class="rules rules-help">
    <h3>What AI can help you do<br>(when approved by your teacher)</h3>
    <ul class="ticks gold col" style="left:36px;top:84px;width:150px">
      <li>Brainstorm ideas</li>
      <li>Read your work aloud using text-to-speech tools</li>
    </ul>
    <ul class="ticks gold col" style="left:220px;top:84px">
      <li>Check spelling, grammar and clarity</li>
      <li>Help identify areas for improvement in a draft</li>
    </ul>
  </section>

  <div class="divider"></div>
  <h2 class="cannot">What You Cannot Do</h2>

  <section class="pieces">
    <div class="piece gold">
      <svg class="no" viewBox="0 0 38 38" aria-hidden="true"><circle cx="19" cy="19" r="18" fill="#fff"/><circle cx="19" cy="19" r="14.5" fill="var(--red)"/><path d="M13 13l12 12M25 13L13 25" stroke="#fff" stroke-width="3.5" stroke-linecap="round"/></svg>
      <span>Submit Algenerated work as your own</span>
      <div class="knob gold right"></div>
    </div>
    <div class="piece navy">
      <svg class="no" viewBox="0 0 38 38" aria-hidden="true"><circle cx="19" cy="19" r="18" fill="#fff"/><circle cx="19" cy="19" r="14.5" fill="var(--red)"/><path d="M13 13l12 12M25 13L13 25" stroke="#fff" stroke-width="3.5" stroke-linecap="round"/></svg>
      <span>Copy and paste AI responseswithout acknowledging or adapting themt</span>
      <div class="knob navy right"></div>
    </div>
    <div class="piece gold">
      <svg class="no" viewBox="0 0 38 38" aria-hidden="true"><circle cx="19" cy="19" r="18" fill="#fff"/><circle cx="19" cy="19" r="14.5" fill="var(--red)"/><path d="M13 13l12 12M25 13L13 25" stroke="#fff" stroke-width="3.5" stroke-linecap="round"/></svg>
      <span>Use AI tools to complete the whole task for you</span>
    </div>
    <div class="piece navy">
      <svg class="no" viewBox="0 0 38 38" aria-hidden="true"><circle cx="19" cy="19" r="18" fill="#fff"/><circle cx="19" cy="19" r="14.5" fill="var(--red)"/><path d="M13 13l12 12M25 13L13 25" stroke="#fff" stroke-width="3.5" stroke-linecap="round"/></svg>
      <span>Submit work that does not demonstrate your understanding</span>
      <div class="knob navy left"></div>
    </div>
  </section>

  <p class="slogan">If you didn't create, develop and understand it, it isn't your work.</p>

  <footer class="footer">
    Marlowe, T. 2025. "Why students don't ask for help- and how to change that" downloaded on 24/04/2026 from https://www.teachforward.org/article/getting-students-ask-help/<br>
    ERIN, 2024. "Supporting self-regulated learning", downloaded on 24/04/2026 from<br>
    https://www.learnevidence.edu/files/2024-02/supporting-self-regulated-learning.pdf
  </footer>
</main>
</body>
</html>
```